Quillmere Business Card

I have a current card that I like it just needs a couple little changes to make it perfect. I would like the font size bigger so it could be easily read by older customers.

Business

```html
<!DOCTYPE html>
<html lang="en">
<head>
<meta charset="utf-8">
<title>Quillmere Motorsport And Marine – Business Card</title>
<link href="https://fonts.googleapis.com/css2?family=Questrial&display=swap" rel="stylesheet">
<style>
  :root {
    --stage: #1e1e1e;
    --stage-edge: #0c0c0c;
    --card: #050505;
    --band-top: #2a2a2a;
    --band-bottom: #141414;
    --green: #3fae2a;
    --white: #f2f2f2;
    --muted: #c9c9c9;
    --faint: #2b2b2b;
    --spring: #8cc63f;
    --summer: #f2c81e;
    --autumn: #b3203c;
    --winter: #2a87b8;
  }
  * { box-sizing: border-box; margin: 0; padding: 0; }
  html, body { width: 1200px; height: 871px; overflow: hidden; }
  body {
    background: radial-gradient(ellipse at 50% 40%, var(--stage) 0%, var(--stage-edge) 100%);
    font-family: "Questrial", "Century Gothic", sans-serif;
    color: var(--white);
    display: flex;
    flex-direction: column;
    align-items: center;
    justify-content: center;
    gap: 36px;
  }
  .card {
    position: relative;
    width: 660px;
    height: 377px;
    background: var(--card);
    box-shadow: 0 18px 40px rgba(0,0,0,.6);
    overflow: hidden;
  }

  /* Front */
  .front-main {
    position: absolute; inset: 0 0 100px 0;
    display: flex;
  }
  .brand {
    width: 300px;
    display: flex; flex-direction: column; align-items: center; justify-content: center;
    gap: 16px;
  }
  .brand-dot {
    width: 64px; height: 64px; border-radius: 50%;
    background: var(--white);
  }
  .brand-name {
    color: var(--green);
    font-size: 19px;
    letter-spacing: .5px;
    text-align: center;
  }
  .contact {
    flex: 1;
    padding: 40px 24px 0 20px;
  }
  .contact-name {
    color: var(--green);
    font-size: 28px;
    letter-spacing: 1px;
    margin-bottom: 16px;
  }
  .address { font-size: 16px; line-height: 1.5; margin-bottom: 14px; }
  .lines { list-style: none; font-size: 16px; line-height: 1.65; }
  .lines li { display: flex; align-items: center; gap: 10px; }
  .lines svg { width: 15px; height: 15px; flex: none; }

  .season-band {
    position: absolute; left: 0; right: 0; bottom: 0; height: 100px;
    background: linear-gradient(var(--band-top), var(--band-bottom));
    display: flex; align-items: center;
    padding: 0 36px;
  }
  .seasons { display: flex; gap: 22px; }
  .season { width: 44px; height: 44px; border-radius: 50%; }
  .season.spring { background: var(--spring); }
  .season.summer { background: var(--summer); }
  .season.autumn { background: var(--autumn); border-radius: 50% 6px; }
  .season.winter { background: var(--winter); }
  .tagline {
    margin-left: auto;
    font-size: 26px;
    letter-spacing: 2px;
    color: var(--muted);
  }

  /* Back */
  .back-mark {
    position: absolute; left: -70px; top: 120px;
    width: 260px; height: 260px; border-radius: 50%;
    background: var(--faint);
  }
  .back-info {
    position: relative;
    text-align: center;
    padding-top: 40px;
  }
  .services { font-size: 17px; line-height: 1.5; letter-spacing: .5px; }
  .website { color: var(--green); font-size: 20px; letter-spacing: 1px; margin: 22px 0 16px; }
  .hours { font-size: 16px; line-height: 1.55; color: var(--muted); }
</style>
</head>
<body>

  <section class="card card-front">
    <div class="front-main">
      <div class="brand">
        <span class="brand-dot"></span>
        <p class="brand-name">Quillmere Motorsport And Marine</p>
      </div>
      <div class="contact">
        <h1 class="contact-name">Dale Harrow</h1>
        <p class="address">4820 Birchwood Lane<br>Ferndale, MN 55000</p>
        <ul class="lines">
          <li>
            <svg viewBox="0 0 16 16" fill="none" stroke="var(--green)" stroke-width="1.4"><rect x="1.5" y="3.5" width="13" height="9"/><path d="M1.5 3.5l6.5 5 6.5-5"/></svg>
            dale@quillmeremotorsports.com
          </li>
          <li>
            <svg viewBox="0 0 16 16" fill="none" stroke="var(--green)" stroke-width="1.4"><path d="M2 6c0-2 2-3 6-3s6 1 6 3l-2.5 1-1-2h-5l-1 2z"/><rect x="4" y="8" width="8" height="5" rx="1"/></svg>
            555 014 2280
          </li>
          <li>
            <svg viewBox="0 0 16 16" fill="none" stroke="var(--green)" stroke-width="1.4"><rect x="4" y="2" width="8" height="4"/><rect x="2" y="6" width="12" height="6" rx="1"/><rect x="4.5" y="10" width="7" height="4"/></svg>
            555 014 2291
          </li>
        </ul>
      </div>
    </div>
    <div class="season-band">
      <div class="seasons">
        <span class="season spring" role="img" aria-label="Green spring flower"></span>
        <span class="season summer" role="img" aria-label="Yellow summer sun"></span>
        <span class="season autumn" role="img" aria-label="Red autumn leaf"></span>
        <span class="season winter" role="img" aria-label="Blue winter snowflake"></span>
      </div>
      <p class="tagline">Fun For All Seasons</p>
    </div>
  </section>

  <section class="card card-back">
    <span class="back-mark"></span>
    <div class="back-info">
      <p class="services">Servicing all makes &amp; models of<br>boats, snowmobiles, motorcycles and ATV's.<br>Custom Welding avalible for alumunium and steel.</p>
      <p class="website">quillmeremotorsports.com</p>
      <p class="hours">Hours :<br>Mon–Tue: 9am - 5:30pm<br>Wed: 9am - 7pm<br>Thu–Fri: 9am - 5:30pm<br>Sat: 9am - 1pm</p>
    </div>
  </section>

</body>
</html>
```